Harlow Funding Real Estate: Golf Membership Card

This golf membership card will be included into the current brochure of Harlow Funding, as shown in the uploaded files (“inside brochure” and “outside brochure”). This membership card will be given as a gift to new clients, when they fund a loan over $1,000,000 with our company. We need the card to be no larger than the following dimensions 5.5 cm in height and 8.5 cm in width. Our company colors are green and red. The card needs to be two sided.
The information to be included in the card is the following:
FRONT:
• Uploaded logos for: “Sutton” and “Verdon”
• "2014"
• Preferably a golf background (green and red colors)
• The following:
o"Membre________________"
Certifier par________________"
• "Cette carte permet l'entrée au membre inscrit, plus un invité" (In small writing, preferably at the bottom of card)
BACK:
• Addresses
o "Les Pins Dorés: Golf et Auberge
872 Route 247 Nord
Sutton, QC J4X 7M3
Telephone: 450-555-0147
www.lespinsdores-exemple.com"
o "Verdon: Golf et Auberge
618 Chemin des Érables
Brownsburg-Chatham, QC
J2R 5T9
Telephone : 450-555-0193
www.golfverdon-exemple.ca"
• Uploaded Logo “Harlow Funding”
• Can be the same as the front background or different
• “Sponsored by Harlow Funding”
Thanks in advance!
Loan

```html
<!DOCTYPE html>
<html lang="fr">
<head>
<meta charset="utf-8">
<title>Harlow Funding – Carte de membre golf 2014</title>
<link rel="stylesheet" href="https://fonts.googleapis.com/css2?family=PT+Sans+Narrow:wght@400;700&family=Marcellus&display=swap">
<style>
  :root{
    --page:#ffffff;
    --grass-light:#8fb24a;
    --grass-dark:#3d5a1c;
    --fairway:#6f8f38;
    --band-green:#1f6b2e;
    --band-green-dark:#135220;
    --turf-red:#7a1a10;
    --turf-red-dark:#4e0e08;
    --gold:#d8c06e;
    --gold-soft:#e0c77a;
    --white:#ffffff;
  }
  *{margin:0;padding:0;box-sizing:border-box}
  html,body{width:1200px;height:920px;overflow:hidden;background:var(--page)}
  body{font-family:"PT Sans Narrow",Arial Narrow,sans-serif}
  .sheet{position:relative;width:1200px;height:920px}
  .card{position:absolute;top:286px;width:540px;height:348px;border-radius:22px;overflow:hidden;box-shadow:0 2px 6px rgba(0,0,0,.25)}
  .card--front{left:40px}
  .card--back{left:620px}
  .card__art{position:absolute;inset:0;width:100%;height:100%}
  .member-fields{position:absolute;left:24px;top:252px;color:var(--gold);font-size:19px;letter-spacing:1.5px;line-height:23px;text-transform:uppercase}
  .partner-marks{position:absolute;left:392px;top:196px;display:flex;gap:10px;align-items:center}
  .partner-mark{display:flex;align-items:center;gap:4px;color:var(--gold);font-size:12px;font-weight:700}
  .partner-mark__dot{width:9px;height:9px;background:var(--gold)}
  .card-year{position:absolute;left:430px;top:268px;font-family:"Marcellus",serif;color:var(--gold);font-size:40px;letter-spacing:1px}
  .entry-note{position:absolute;left:0;right:0;bottom:0;height:22px;line-height:22px;text-align:center;color:var(--white);font-size:12px;font-weight:700}
  .venue{position:absolute;top:44px;color:var(--gold-soft);font-size:14.5px;line-height:19px}
  .venue--pins{left:62px}
  .venue--verdon{left:318px}
  .sponsor{position:absolute;right:22px;bottom:22px;text-align:right;color:var(--white)}
  .sponsor__label{font-size:12px}
  .sponsor__name{display:flex;align-items:center;gap:5px;font-size:16px;font-weight:700}
  .sponsor__dot{width:9px;height:9px;border-radius:50%;background:var(--white)}
</style>
</head>
<body>
<main class="sheet">

  <section class="card card--front" aria-label="Recto de la carte de membre">
    <svg class="card__art" viewBox="0 0 540 348" preserveAspectRatio="none">
      <defs>
        <linearGradient id="front-photo" x1="0" y1="0" x2="0" y2="1">
          <stop offset="0" stop-color="var(--fairway)"/>
          <stop offset=".45" stop-color="var(--grass-light)"/>
          <stop offset="1" stop-color="var(--grass-dark)"/>
        </linearGradient>
        <linearGradient id="front-turf" x1="0" y1="0" x2="0" y2="1">
          <stop offset="0" stop-color="var(--turf-red)"/>
          <stop offset="1" stop-color="var(--turf-red-dark)"/>
        </linearGradient>
      </defs>
      <rect class="golf-photo" role="img" aria-label="Photo d’une balle de golf posée dans l’herbe d’un parcours" width="540" height="240" fill="url(#front-photo)"/>
      <path class="green-sweep" d="M0 196 C160 214 360 190 540 128 L540 348 L0 348 Z" fill="var(--band-green)"/>
      <path class="red-turf" role="img" aria-label="Texture d’herbe teintée rouge" d="M0 210 C170 228 370 204 540 144 L540 348 L0 348 Z" fill="url(#front-turf)"/>
      <rect class="entry-strip" y="326" width="540" height="22" fill="var(--band-green)"/>
    </svg>
    <div class="member-fields">
      <p>Membre</p>
      <p>Certifier par</p>
    </div>
    <div class="partner-marks">
      <span class="partner-mark"><span class="partner-mark__dot"></span>Verdon</span>
      <span class="partner-mark"><span class="partner-mark__dot"></span>Les Pins Dorés</span>
    </div>
    <p class="card-year">2014</p>
    <p class="entry-note">Cette carte permet l’entrée au membre inscrit, plus un invité</p>
  </section>

  <section class="card card--back" aria-label="Verso de la carte de membre">
    <svg class="card__art" viewBox="0 0 540 348" preserveAspectRatio="none">
      <defs>
        <linearGradient id="back-photo" x1="0" y1="0" x2="0" y2="1">
          <stop offset="0" stop-color="#2c3f16"/>
          <stop offset=".6" stop-color="#3a5219"/>
          <stop offset="1" stop-color="#22330f"/>
        </linearGradient>
        <linearGradient id="back-turf" x1="0" y1="0" x2="0" y2="1">
          <stop offset="0" stop-color="var(--turf-red)"/>
          <stop offset="1" stop-color="var(--turf-red-dark)"/>
        </linearGradient>
      </defs>
      <rect class="golf-photo" role="img" aria-label="Photo assombrie d’un parcours de golf" width="540" height="240" fill="url(#back-photo)"/>
      <path class="green-sweep" d="M0 206 C170 222 370 202 540 160 L540 348 L0 348 Z" fill="var(--band-green-dark)"/>
      <path class="red-turf" role="img" aria-label="Texture d’herbe teintée rouge" d="M0 220 C175 236 375 216 540 176 L540 348 L0 348 Z" fill="url(#back-turf)"/>
    </svg>
    <address class="venue venue--pins" style="font-style:normal">
      Les Pins Dorés: Golf et Auberge<br>
      872 Route 247 Nord<br>
      Sutton, QC J4X 7M3<br>
      Telephone: 450-555-0147<br>
      www.lespinsdores-exemple.com
    </address>
    <address class="venue venue--verdon" style="font-style:normal">
      Verdon: Golf et Auberge<br>
      618 Chemin des Érables<br>
      Brownsburg-Chatham, QC<br>
      J2R 5T9<br>
      Telephone : 450-555-0193<br>
      www.golfverdon-exemple.ca
    </address>
    <div class="sponsor">
      <p class="sponsor__label">Sponsored by</p>
      <p class="sponsor__name"><span class="sponsor__dot"></span>Harlow Funding</p>
    </div>
  </section>

</main>
</body>
</html>
```